Global Outreach Fellowship needs a Book Cover Design Project

I am a pastor, missionary, author, and the founder of a non-profit organization. I am in the process of publishing a book focused on "The Soul of a Faithful Shepherd" and desire a contemporary, even somewhat abstract book cover. Here is a link to the company's web page portfolio that designed our Web Page, to give you an idea of the style of cover that I am looking for. http://www.pixelharborstudio.com/cd-covers

Though the book is obviously targeted toward Christians, I want it to be attractive enough to capture the attention of the general population as well.

Industry/Entity Type

Non-Profit

```html
<!DOCTYPE html>
<html lang="en">
<head>
<meta charset="utf-8">
<title>The Soul of a Faithful Shepherd – Book Cover</title>
<link rel="stylesheet" href="https://fonts.googleapis.com/css2?family=Oswald:wght@500;700&family=PT+Sans:wght@400;700&display=swap">
<style>
  :root {
    --page-bg: #e9e9e9;
    --ink: #000000;
    --paper: #ffffff;
    --ember-red: #b3150a;
    --flame-deep: #c2380c;
    --flame-mid: #ee7a22;
    --flame-light: #ffd9a8;
    --back-dark: #4a1a0c;
    --back-mid: #7b3b1c;
    --back-grey: #8d8580;
    --spine-light: #fff6ef;
    --spine-peach: #f7cdb0;
  }

  * { box-sizing: border-box; margin: 0; padding: 0; }

  html, body {
    width: 1200px;
    height: 845px;
    overflow: hidden;
    background: var(--page-bg);
  }

  .book-wrap {
    position: absolute;
    left: 58px;
    top: 20px;
    width: 1084px;
    height: 806px;
    display: flex;
    box-shadow: 0 2px 6px rgba(0, 0, 0, 0.25);
  }

  /* ---------- Back cover ---------- */
  .back-cover {
    position: relative;
    width: 504px;
    height: 806px;
    overflow: hidden;
    background: var(--ink);
  }

  .back-art {
    position: absolute;
    left: 0; top: 0;
    width: 504px;
    height: 694px;
    background:
      radial-gradient(ellipse 60% 55% at 60% 50%, rgba(141, 133, 128, 0.85), rgba(141, 133, 128, 0) 75%),
      linear-gradient(160deg, var(--back-dark) 0%, var(--back-mid) 40%, #6b3219 70%, var(--back-dark) 100%);
  }

  .back-title {
    position: absolute;
    left: 90px;
    top: 40px;
    width: 340px;
    text-align: center;
    font-family: "Oswald", sans-serif;
    font-weight: 700;
    color: var(--paper);
    -webkit-text-stroke: 3px var(--ink);
    paint-order: stroke fill;
    text-transform: uppercase;
  }
  .back-title .line-top { font-size: 34px; line-height: 50px; }
  .back-title .line-top .big { font-size: 52px; }
  .back-title .line-main { font-size: 66px; line-height: 64px; }
  .back-title .line-tail { font-size: 32px; line-height: 40px; letter-spacing: 12px; margin-left: 12px; }

  .back-copy {
    position: absolute;
    left: 34px;
    top: 226px;
    width: 432px;
    color: var(--paper);
    font-family: "PT Sans", sans-serif;
    text-shadow: 0 0 2px rgba(0, 0, 0, 0.5);
  }
  .back-copy h2 {
    font-weight: 400;
    font-size: 24px;
    line-height: 32px;
    margin-bottom: 10px;
    letter-spacing: -0.4px;
  }
  .back-copy p {
    font-size: 10.8px;
    line-height: 15.4px;
    font-weight: 700;
    margin-bottom: 15px;
  }

  /* ---------- Spine ---------- */
  .spine {
    position: relative;
    width: 76px;
    height: 806px;
    background: linear-gradient(90deg, var(--spine-light) 0%, var(--spine-light) 30%, var(--spine-peach) 100%);
    font-family: "Oswald", sans-serif;
    color: var(--ink);
    text-transform: uppercase;
  }
  .spine-title {
    position: absolute;
    left: 18px;
    top: 44px;
    writing-mode: vertical-rl;
    font-weight: 700;
    font-size: 29px;
    line-height: 40px;
    letter-spacing: 0.4px;
    white-space: nowrap;
  }
  .spine-author {
    position: absolute;
    left: 24px;
    top: 642px;
    writing-mode: vertical-rl;
    font-weight: 700;
    font-size: 18px;
    line-height: 28px;
    text-transform: none;
    white-space: nowrap;
  }

  /* ---------- Front cover ---------- */
  .front-cover {
    position: relative;
    width: 504px;
    height: 806px;
    overflow: hidden;
  }
  .front-art {
    position: absolute;
    inset: 0;
    background:
      radial-gradient(ellipse 55% 35% at 45% 22%, rgba(150, 120, 70, 0.8), rgba(150, 120, 70, 0) 80%),
      radial-gradient(ellipse 40% 30% at 8% 30%, rgba(255, 255, 255, 0.9), rgba(255, 255, 255, 0) 80%),
      radial-gradient(ellipse 70% 40% at 60% 75%, var(--flame-light), rgba(255, 217, 168, 0) 70%),
      linear-gradient(170deg, var(--flame-deep) 0%, var(--flame-mid) 35%, #f59a45 60%, var(--flame-mid) 85%, #d9501a 100%);
  }

  .front-title {
    position: absolute;
    left: 0;
    top: 436px;
    width: 504px;
    text-align: center;
    font-family: "Oswald", sans-serif;
    font-weight: 700;
    color: var(--ink);
    text-transform: uppercase;
    -webkit-text-stroke: 5px var(--paper);
    paint-order: stroke fill;
    text-shadow: 0 0 2px var(--ember-red), 1px 1px 1px var(--ember-red), -1px -1px 1px var(--ember-red);
  }
  .front-title .line-top { font-size: 46px; line-height: 70px; }
  .front-title .line-top .big { font-size: 74px; }
  .front-title .line-main { font-size: 88px; line-height: 84px; }
  .front-title .line-tail { font-size: 48px; line-height: 56px; letter-spacing: 22px; margin-left: 22px; }

  .front-author {
    position: absolute;
    right: 48px;
    top: 754px;
    font-family: "Oswald", sans-serif;
    font-weight: 700;
    font-size: 22px;
    color: var(--paper);
    text-shadow: 0 0 3px rgba(120, 30, 0, 0.6);
  }
</style>
</head>
<body>
  <main class="book-wrap">

    <section class="back-cover">
      <div class="back-art" role="img" aria-label="Back cover artwork in dark warm tones"></div>

      <h1 class="back-title">
        <div class="line-top">The <span class="big">Soul</span> of a</div>
        <div class="line-main">Faithful</div>
        <div class="line-tail">Shepherd</div>
      </h1>

      <div class="back-copy">
        <h2>Lorem ipsum dolor sit amet</h2>
        <p>Lorem ipsum dolor sit amet, consectetuer adipiscing elit, sed diam nonummy nibh euismod tincidunt ut laoreet dolore magna aliquam erat volutpat. Ut wisi enim ad minim veniam, quis nostrud exerci tation ullamcorper suscipit lobortis nisl ut aliquip ex ea commodo consequat. Duis autem vel eum iriure dolor in hendrerit in vulputate velit esse molestie consequat, vel illum dolore eu feugiat nulla facilisis at vero eros et accumsan et iusto odio dignissim qui blandit praesent luptatum zzril delenit augue duis dolore te feugait nulla facilisi.</p>
        <p>Lorem ipsum dolor sit amet, consectetuer adipiscing elit, sed diam nonummy nibh euismod tincidunt ut laoreet dolore magna aliquam erat volutpat. Ut wisi enim ad minim veniam, quis nostrud exerci tation ullamcorper suscipit lobortis nisl ut aliquip ex ea commodo consequat. Duis autem vel eum iriure dolor in hendrerit in vulputate velit esse molestie consequat, vel illum dolore eu feugiat nulla facilisis at vero eros et accumsan et iusto odio dignissim qui blandit praesent luptatum zzril delenit augue duis dolore te feugait nulla facilisi.</p>
        <p>Lorem ipsum dolor sit amet, consectetuer adipiscing elit, sed diam nonummy nibh euismod tincidunt ut laoreet dolore magna aliquam erat volutpat. Ut wisi enim ad minim veniam, quis nostrud exerci tation ullamcorper suscipit lobortis nisl ut aliquip ex ea commodo consequat. Duis autem vel eum iriure dolor in hendrerit in vulputate velit esse molestie consequat, vel illum dolore eu feugiat nulla facilisis at vero eros et accumsan et iusto odio dignissim qui blandit praesent luptatum zzril delenit augue duis dolore te feugait nulla facilisi.</p>
      </div>
    </section>

    <section class="spine">
      <div class="spine-title">The Soul of a Faithful Shepherd</div>
      <div class="spine-author">Daniel Whitmore</div>
    </section>

    <section class="front-cover">
      <div class="front-art" role="img" aria-label="Front cover artwork in bright orange tones"></div>
      <h2 class="front-title">
        <div class="line-top">The <span class="big">Soul</span> of a</div>
        <div class="line-main">Faithful</div>
        <div class="line-tail">Shepherd</div>
      </h2>
      <div class="front-author">Daniel Whitmore</div>
    </section>

  </main>
</body>
</html>
```